Modern Corporate Brochure For Australian Real Estate Agency

We need a corporate 10 page A4 brochure for a Australian Real Estate agency with information for our clients and referral partners.

Main colour scheme: #238b53

Examples of designs:
https://plorvendax.example/item/8-page-corporate-business-brochure/5820417

https://plorvendax.example/item/brochure/7461283

https://plorvendax.example/item/the-company-profile/39851620

https://plorvendax.example/item/brochure-pack-a4trifold-leafletbusiness-card/857312

Target Market(s)

Professional Australians

Industry/Entity Type

Real Estate

Font styles to use
Sans Serif

Requirements
Must have
• Use of multiple greens from the logo

```html
<!DOCTYPE html>
<html lang="en">
<head>
<meta charset="utf-8">
<title>Halvern Property Group – Brochure Spreads</title>
<link href="https://fonts.googleapis.com/css2?family=Open+Sans:ital,wght@0,300;0,400;0,600;0,700;1,600&display=swap" rel="stylesheet">
<style>
:root{
  --green:#238b53;
  --green-dark:#1a6b3f;
  --green-mid:#3aa060;
  --green-light:#8cc63f;
  --lime:#d4ebb4;
  --stage:#3c4a3b;
  --paper:#f6f6f4;
  --ink:#4a4a4a;
  --ink-soft:#6a6a6a;
  --band:#5e5e5e;
  --white:#ffffff;
}
*{box-sizing:border-box;margin:0;padding:0}
html,body{width:1200px;height:4000px;overflow:hidden}
body{background:var(--stage);font-family:"Open Sans",Arial,sans-serif;color:var(--ink);position:relative}
.spread{position:absolute;left:133px;width:934px;height:660px;background:var(--paper);box-shadow:0 10px 28px rgba(0,0,0,.45);overflow:hidden}
.page{position:absolute;top:0;width:467px;height:660px}
.page.left{left:0}.page.right{left:467px;background:var(--white)}
.abs{position:absolute}
.photo{position:absolute}
.ph-house{background:linear-gradient(180deg,#9cc0de 0%,#c9dbe6 40%,#8a8470 62%,#4f7a3a 100%)}
.ph-house.b{background:linear-gradient(180deg,#b7cfe0 0%,#d9d6cc 45%,#6d7a5c 70%,#3f6a2c 100%)}
.ph-house.c{background:linear-gradient(180deg,#8fb6d6 0%,#eef0ee 45%,#a8a8a0 65%,#4c7d34 100%)}
.ph-house.d{background:linear-gradient(180deg,#2d3c5a 0%,#5a5f6e 45%,#b58a52 68%,#3a4a2c 100%)}
.ph-city{background:linear-gradient(180deg,#cfdce6 0%,#aebfcc 50%,#7f95a8 62%,#c9d3da 100%)}
.ph-tower{background:linear-gradient(160deg,#dfe8ef 0%,#9fb3c3 50%,#6c8296 100%)}
.tab{position:absolute;height:30px;background:var(--green);color:var(--white);font-weight:700;font-size:13px;line-height:30px;padding-left:32px;clip-path:polygon(0 0,100% 0,calc(100% - 26px) 100%,0 100%)}
.tab-stripe{position:absolute;top:0;height:30px;width:12px;background:var(--green);transform:skewX(-40deg)}
.hex{width:66px;height:74px;clip-path:polygon(50% 0,100% 25%,100% 75%,50% 100%,0 75%,0 25%);background:var(--green);display:flex;align-items:center;justify-content:center;margin:0 auto}
.hex svg{width:34px;height:34px;fill:none;stroke:var(--white);stroke-width:1.6;stroke-linecap:round;stroke-linejoin:round}
.service{position:absolute;text-align:center}
.service h4{font-size:10.5px;font-weight:600;color:#333;line-height:15px;margin-top:14px}
.service p{font-size:8.4px;line-height:12.6px;color:var(--ink);text-align:justify;margin-top:14px}
h2.section{font-size:19px;font-weight:400;color:#333;border-bottom:1.5px solid #333;display:inline-block;padding-bottom:2px}
.body{font-size:8.4px;line-height:12.6px;text-align:justify}
/* cover */
.cover-title{position:absolute;left:22px;top:370px;color:var(--white);font-size:37px;line-height:41px;font-weight:300}
.cover-title b{font-weight:700}
.brand-mark{width:20px;height:20px;background:var(--green)}
.brand-name{font-size:21px;font-weight:600;color:#333;letter-spacing:.2px}
.brand-tag{font-size:10px;letter-spacing:.6px;color:#666}
.testimonial{position:absolute;left:44px;width:306px;font-size:8.4px;line-height:13px;color:var(--ink)}
.testimonial .q{font-size:22px;font-weight:700;color:#333;line-height:14px;display:block;height:12px}
.testimonial .by{float:right;margin-top:-2px;font-size:9.5px}
.contact li{list-style:none;font-size:9.8px;line-height:14px;position:relative;padding-left:18px;margin-bottom:7px;color:#333}
.contact li svg{position:absolute;left:0;top:1px;width:13px;height:13px}
/* about */
.about-panel{position:absolute;left:0;top:0;width:467px;height:455px;background:var(--green);color:var(--white);padding:40px 28px 0 28px}
.about-panel h2{font-size:19px;font-weight:400;border-bottom:1.5px solid var(--white);display:inline-block;padding-bottom:1px;margin-bottom:18px}
.about-panel p{font-size:8.9px;line-height:13.1px;text-align:justify;margin-bottom:12px}
.stat{position:absolute;top:473px;width:90px;text-align:center;font-size:9.6px;font-weight:600;line-height:13px;color:#333}
.stat .hex{margin-bottom:6px}
.pm-head{position:absolute;left:110px;top:22px;width:248px;height:22px;background:var(--green);color:var(--white);font-weight:700;font-size:12.5px;text-align:center;line-height:22px}
.pm-rule{position:absolute;top:33px;height:2px;background:var(--green)}
.green-lead{font-size:9px;font-weight:600;color:var(--green)}
.col3 h5{font-size:10px;font-weight:600;color:#333;text-align:center;margin-bottom:8px}
/* services */
.services-band{position:absolute;left:0;top:220px;width:934px;height:233px;background:var(--band)}
.svc{position:absolute;top:42px;width:124px;text-align:center;color:#eee}
.svc h4{font-size:11.5px;font-weight:400;margin:14px 0 10px}
.svc p{font-size:7.8px;line-height:11.5px;color:#e2e2e2}
/* house & land */
.list-head{position:absolute;left:36px;font-size:10px;font-weight:600;color:var(--green)}
.list{position:absolute;left:36px;width:390px}
.list li{list-style:none;font-size:8.8px;line-height:16.6px;color:#333;position:relative;padding-left:16px}
.list li::before{content:"";position:absolute;left:0;top:4px;width:8px;height:8px;border:1px solid var(--green);border-radius:50%}
.list li span{position:absolute;left:302px}
.opt{position:absolute;top:488px;width:130px}
.opt h5{font-size:10px;font-weight:600;color:var(--green);margin-bottom:10px}
.opt li{list-style:none;font-size:8.8px;line-height:17px;color:#333;position:relative;padding-left:16px}
.opt li::before{content:"";position:absolute;left:0;top:4px;width:8px;height:8px;border:1px solid var(--green);border-radius:50%}
</style>
</head>
<body>

<!-- Spread 1: back cover + front cover -->
<section class="spread" style="top:120px">
  <div class="page left">
    <div class="photo" role="img" aria-label="Night city skyline photo overlaid with green triangle mosaic" style="left:0;top:0;width:467px;height:330px;background:linear-gradient(165deg,#0e2a1b 0%,#1d5a36 40%,#3a9a4e 70%,#f6f6f4 71%)"></div>
    <h3 class="abs" style="left:44px;top:307px;font-size:14px;font-weight:600;color:var(--green-dark)">Testimonials</h3>
    <div class="testimonial" style="top:332px">
      <span class="q">&ldquo;</span>
      Lorem ipsum dolor sit amet, consectetur adipiscing elit, sed do eiusmod tempor incididunt ut labore et dolore magna aliqua. Ut enim ad minim veniam, quis nostrud exercitation ullamco laboris.
      <span class="by">- Sam Reed <b style="font-size:16px">&rdquo;</b></span>
    </div>
    <div class="testimonial" style="top:402px">
      <span class="q">&ldquo;</span>
      Lorem ipsum dolor sit amet, consectetur adipiscing elit, sed do eiusmod tempor incididunt ut labore et dolore magna aliqua. Ut enim ad minim veniam, quis nostrud exercitation ullamco laboris.
      <span class="by">- Sam Reed <b style="font-size:16px">&rdquo;</b></span>
    </div>
    <div class="abs" style="left:44px;top:475px;width:340px;height:1px;background:#ccc"></div>
    <h3 class="abs" style="left:44px;top:505px;font-size:14px;font-weight:600;color:var(--green-dark)">Contact Info</h3>
    <ul class="contact abs" style="left:44px;top:535px;width:220px">
      <li><svg viewBox="0 0 16 16"><path d="M8 1a5 5 0 0 0-5 5c0 4 5 9 5 9s5-5 5-9a5 5 0 0 0-5-5z" fill="#238b53"/><circle cx="8" cy="6" r="2" fill="#fff"/></svg>27 Marlow Lane, Fortitude Valley, Brisbane</li>
      <li><svg viewBox="0 0 16 16"><rect x="1" y="3" width="14" height="10" rx="1" fill="#238b53"/><path d="M1 4l7 5 7-5" stroke="#fff" fill="none"/></svg>info@halvernproperty.example</li>
      <li><svg viewBox="0 0 16 16"><circle cx="8" cy="8" r="7" fill="#238b53"/><path d="M5 4c0 4 3 7 7 7l0-2-2-.5-1 1c-1-.5-2-1.5-2.5-2.5l1-1L7 4z" fill="#fff"/></svg>(07) 5550 1847</li>
      <li><svg viewBox="0 0 16 16"><circle cx="8" cy="8" r="7" fill="#238b53"/><circle cx="8" cy="8" r="4.5" stroke="#fff" fill="none"/><line x1="3.5" y1="8" x2="12.5" y2="8" stroke="#fff"/></svg>www.halvernproperty.example</li>
    </ul>
    <div class="photo" role="img" aria-label="Green triangle mosaic corner" style="left:400px;top:590px;width:67px;height:70px;background:linear-gradient(135deg,transparent 50%,var(--green-mid) 50%)"></div>
  </div>
  <div class="page right">
    <div class="photo" role="img" aria-label="Light green triangle mosaic" style="left:310px;top:0;width:157px;height:260px;background:linear-gradient(200deg,#bfe59a 0%,#e8f3dc 60%,#ffffff 100%)"></div>
    <div class="abs brand-mark" style="left:40px;top:113px"></div>
    <div class="abs brand-name" style="left:68px;top:107px">Halvern Property Group</div>
    <div class="abs brand-tag" style="left:40px;top:160px;width:300px">Residential · Commercial · Holiday Rentals</div>
    <div class="photo" role="img" aria-label="City river at dusk with light-trail traffic" style="left:0;top:240px;width:467px;height:420px;background:linear-gradient(180deg,#2b4f9a 0%,#3b5fa8 35%,#6a6f9a 55%,#2c2a40 75%,#d66b2c 85%,#1d1d2a 100%)"></div>
    <h1 class="cover-title">A <b>New Level</b><br>of Service in<br><b>PROPERTY</b></h1>
    <div class="abs" style="right:44px;top:608px;color:#fff;font-size:11px">www.halvernproperty.example</div>
  </div>
  <svg class="abs" style="left:0;top:0" width="934" height="660" viewBox="0 0 934 660" aria-hidden="true">
    <polygon points="150,110 934,360 934,405 110,158" fill="var(--green)"/>
    <polygon points="300,140 934,345 934,360 280,150" fill="#1b5e38"/>
    <polygon points="467,210 560,240 467,280" fill="var(--green-light)" opacity=".8"/>
    <polygon points="467,600 540,660 467,660" fill="var(--green)"/>
  </svg>
</section>

<!-- Spread 2 -->
<section class="spread" style="top:905px">
  <div class="page left">
    <div class="tab" style="left:0;top:19px;width:330px">Brisbane's Leading Property Group</div>
    <div class="tab-stripe" style="left:340px;top:19px"></div>
    <div class="service" style="left:29px;top:63px;width:190px">
      <div class="hex"><svg viewBox="0 0 32 32"><path d="M5 15 16 6l11 9"/><rect x="8" y="14" width="16" height="12"/><rect x="14" y="19" width="4" height="7"/><rect x="10" y="17" width="3" height="3"/><rect x="19" y="17" width="3" height="3"/></svg></div>
      <h4>Brisbane Property<br>Management</h4>
      <p>Our average vacancy rate at any given time is under 5% and our properties generate 6% higher rents than our competitors.</p>
    </div>
    <div class="service" style="left:247px;top:63px;width:190px">
      <div class="hex"><svg viewBox="0 0 32 32"><rect x="6" y="20" width="4" height="6"/><rect x="12" y="16" width="4" height="10"/><rect x="18" y="12" width="4" height="14"/><polyline points="6,14 14,9 20,10 26,5"/><polyline points="22,5 26,5 26,9"/></svg></div>
      <h4>Brisbane<br>Property Sales</h4>
      <p>Only elite agents with the right approach to dealing with people in real estate are offered the opportunity to sell through Halvern Property Group.</p>
    </div>
    <div class="service" style="left:29px;top:273px;width:190px">
      <div class="hex"><svg viewBox="0 0 32 32"><rect x="5" y="6" width="22" height="15"/><polyline points="8,17 13,12 17,15 23,9"/><line x1="16" y1="21" x2="16" y2="25"/><line x1="11" y1="26" x2="21" y2="26"/></svg></div>
      <h4>Brisbane Project<br>Marketing</h4>
      <p>We work closely with a number of large and reputable marketing agencies and companies that have the capacity to deliver a large number of sales.</p>
    </div>
    <div class="service" style="left:247px;top:273px;width:190px">
      <div class="hex"><svg viewBox="0 0 32 32"><rect x="6" y="5" width="20" height="15"/><polyline points="9,16 14,11 18,14 23,8"/><line x1="16" y1="20" x2="11" y2="27"/><line x1="16" y1="20" x2="21" y2="27"/></svg></div>
      <h4>Brisbane Development<br>Management</h4>
      <p>Development management is a niche skill and takes both the academic knowhow and experience to deliver the project through to completion.</p>
    </div>
    <div class="photo ph-city" role="img" aria-label="City skyline reflected on water" style="left:0;top:480px;width:231px;height:180px"></div>
    <div class="abs" style="left:231px;top:480px;width:5px;height:180px;background:var(--green)"></div>
    <div class="photo ph-tower" role="img" aria-label="Glass office tower seen from below" style="left:236px;top:480px;width:231px;height:180px"></div>
  </div>
  <div class="page right">
    <div class="photo ph-house" role="img" aria-label="Two-storey suburban house" style="left:0;top:0;width:231px;height:147px"></div>
    <div class="photo ph-house b" role="img" aria-label="House with lit windows at dusk" style="left:236px;top:0;width:231px;height:147px"></div>
    <div class="photo ph-house c" role="img" aria-label="White weatherboard house with lawn" style="left:0;top:151px;width:231px;height:147px"></div>
    <div class="photo ph-house d" role="img" aria-label="Modern family home at twilight" style="left:236px;top:151px;width:231px;height:147px"></div>
    <div class="tab" style="left:0;top:306px;width:410px">Gladstone's Fastest Growing Property Group</div>
    <div class="tab-stripe" style="left:420px;top:306px"></div>
    <div class="service" style="left:31px;top:346px;width:190px">
      <div class="hex"><svg viewBox="0 0 32 32"><path d="M5 15 16 6l11 9"/><rect x="8" y="14" width="16" height="12"/><rect x="14" y="19" width="4" height="7"/><rect x="10" y="17" width="3" height="3"/><rect x="19" y="17" width="3" height="3"/></svg></div>
      <h4>Gladstone Property<br>Management</h4>
      <p>It is common to find that within the overwhelming majority of real estate offices the property management department is the most under resourced. It's no wonder investors move from one agency to another in search of a decent property manager and agency to work with.</p>
    </div>
    <div class="service" style="left:248px;top:346px;width:190px">
      <div class="hex"><svg viewBox="0 0 32 32"><rect x="6" y="20" width="4" height="6"/><rect x="12" y="16" width="4" height="10"/><rect x="18" y="12" width="4" height="14"/><polyline points="6,14 14,9 20,10 26,5"/><polyline points="22,5 26,5 26,9"/></svg></div>
      <h4>Gladstone<br>Property Sales</h4>
      <p>When selling your property it is important to select an agent who is a part of an agency with a great culture and proven results in selling property regardless of market conditions. Our sales consultants have been selected to work within the Halvern Property brand as they have experience within the industry and have constantly outperformed.</p>
    </div>
  </div>
</section>

<!-- Spread 3 -->
<section class="spread" style="top:1672px">
  <div class="page left" style="background:var(--white)">
    <div class="about-panel">
      <h2>About us</h2>
      <p>Halvern Property Group are forward thinking property specialists, changing the perception of the property industry with our proven strategies, to ensure the success of your assets. With a focus on achieving superior results, our team of highly experienced Property Managers aim to deliver outstanding service to our clients and customers.</p>
      <p>Having your property managed correctly and professionally is important to the success and performance achieved by your investment. A qualified and well-structured agency is crucial for this outcome.</p>
      <p>Our experienced team of Property Managers are attentive, determined, and accountable. We understand the importance of transparent communication and commitment to our clients. Our team collectively have over 80 years' experience in Property Management, we influence our industry's durability and knowledge to our client's advantage.</p>
      <p>The origin of Halvern Property Group is a humble one, when it was founded by two young students Marcus Ellery and Owen Prescott working from shared office in Woolloongabba. It opened its doors to new clients and partners alike on the 6th of August 2012. The focus from the very beginning was to do things differently and build one of Brisbane's first property management specialist companies!</p>
    </div>
    <div class="stat" style="left:19px"><div class="hex"><svg viewBox="0 0 32 32"><rect x="6" y="5" width="14" height="18"/><line x1="9" y1="10" x2="17" y2="10"/><line x1="9" y1="14" x2="17" y2="14"/><rect x="14" y="17" width="12" height="10"/></svg></div>55% faster<br>lease renewals</div>
    <div class="stat" style="left:131px"><div class="hex"><svg viewBox="0 0 32 32"><circle cx="16" cy="11" r="5"/><path d="M7 27c0-5 4-9 9-9s9 4 9 9"/><path d="M16 18v5"/></svg></div>Full Service<br>Agency</div>
    <div class="stat" style="left:239px"><div class="hex"><svg viewBox="0 0 32 32"><circle cx="18" cy="13" r="7"/><line x1="13" y1="18" x2="6" y2="25"/><path d="M15 13h6M18 10v6"/></svg></div>2% Vacancy</div>
    <div class="stat" style="left:351px"><div class="hex"><svg viewBox="0 0 32 32"><rect x="5" y="10" width="22" height="13" rx="1"/><circle cx="16" cy="16.5" r="3"/><path d="M8 7h16"/></svg></div>5% rent<br>arrears</div>
  </div>
  <div class="page right">
    <div class="pm-rule" style="left:30px;width:80px"></div>
    <div class="pm-rule" style="left:358px;width:90px"></div>
    <div class="pm-head">PROPERTY MANAGEMENT</div>
    <svg class="abs process-flow" style="left:14px;top:62px" width="440" height="270" viewBox="0 0 440 270" font-family="Open Sans, sans-serif" font-size="7" font-weight="600" text-anchor="middle" aria-label="Fifteen-step property management process">
      <defs><marker id="arr" markerWidth="6" markerHeight="6" refX="5" refY="3" orient="auto"><path d="M0 0L6 3L0 6z" fill="#8a8a8a"/></marker></defs>
      <g stroke="#8a8a8a" stroke-width="1.2" marker-end="url(#arr)">
        <line x1="82" y1="33" x2="90" y2="33"/><line x1="170" y1="33" x2="178" y2="33"/><line x1="258" y1="33" x2="266" y2="33"/><line x1="346" y1="33" x2="354" y2="33"/>
        <line x1="395" y1="56" x2="395" y2="102"/>
        <line x1="356" y1="127" x2="348" y2="127"/><line x1="268" y1="127" x2="260" y2="127"/><line x1="180" y1="127" x2="172" y2="127"/><line x1="92" y1="127" x2="84" y2="127"/>
        <line x1="43" y1="150" x2="43" y2="196"/>
        <line x1="82" y1="221" x2="90" y2="221"/><line x1="170" y1="221" x2="178" y2="221"/><line x1="258" y1="221" x2="266" y2="221"/><line x1="346" y1="221" x2="354" y2="221"/>
      </g>
      <g>
        <rect x="4" y="10" width="78" height="46" rx="3" fill="#1a6b3f"/><rect x="92" y="10" width="78" height="46" rx="3" fill="#238b53"/><rect x="180" y="10" width="78" height="46" rx="3" fill="#3aa060"/><rect x="268" y="10" width="78" height="46" rx="3" fill="#238b53"/><rect x="356" y="10" width="78" height="46" rx="3" fill="#1a6b3f"/>
        <rect x="356" y="104" width="78" height="46" rx="3" fill="#6fb43f"/><rect x="268" y="104" width="78" height="46" rx="3" fill="#3aa060"/><rect x="180" y="104" width="78" height="46" rx="3" fill="#238b53"/><rect x="92" y="104" width="78" height="46" rx="3" fill="#3aa060"/><rect x="4" y="104" width="78" height="46" rx="3" fill="#6fb43f"/>
        <rect x="4" y="198" width="78" height="46" rx="3" fill="#1a6b3f"/><rect x="92" y="198" width="78" height="46" rx="3" fill="#238b53"/><rect x="180" y="198" width="78" height="46" rx="3" fill="#3aa060"/><rect x="268" y="198" width="78" height="46" rx="3" fill="#238b53"/><rect x="356" y="198" width="78" height="46" rx="3" fill="#1a6b3f"/>
      </g>
      <g fill="#fff">
        <text x="43" y="31">1. Rental Market</text><text x="43" y="41">Appraisal</text>
        <text x="131" y="31">2. Property listed</text><text x="131" y="41">for Rent</text>
        <text x="219" y="31">3. Viewings &amp;</text><text x="219" y="41">Open Homes</text>
        <text x="307" y="31">4. Tenant</text><text x="307" y="41">Application</text>
        <text x="395" y="31">5. Securing a</text><text x="395" y="41">Tenant</text>
        <text x="395" y="125">6. Entry Condition</text><text x="395" y="135">Inspection</text>
        <text x="307" y="125">7. Move In New</text><text x="307" y="135">Tenants</text>
        <text x="219" y="125">8. Rental income</text><text x="219" y="135">collection</text>
        <text x="131" y="125">9. Managing</text><text x="131" y="135">Maintenance</text>
        <text x="43" y="125">10. Regular</text><text x="43" y="135">Inspections</text>
        <text x="43" y="219">11. Managing</text><text x="43" y="229">Lease Renewals</text>
        <text x="131" y="219">12. Billing &amp;</text><text x="131" y="229">Invoices</text>
        <text x="219" y="219">13. Tenant gives</text><text x="219" y="229">Notice to vacate</text>
        <text x="307" y="219">14. Bond Cleaning</text><text x="307" y="229">by Tenant</text>
        <text x="395" y="219">15. Exit Condition</text><text x="395" y="229">Inspection</text>
      </g>
    </svg>
    <div class="abs green-lead" style="left:30px;top:348px">Our Property Management Department is our number one focus!</div>
    <div class="abs body" style="left:30px;top:370px;width:410px">
      <p style="margin-bottom:8px">Here at Halvern Property Group we value our clients and only want to provide the best service possible, which is why we only employ the best in the industry. We provide our team with regular industry training to ensure they are aware of all legislative changes, which allows our Property Managers to deal with any challenges that come their way, comfortably and efficiently.</p>
      <p>We understand what is involved with managing properties, from A-Z and that is why we're a Full-Service Agency. While we are busy talking legislation, our clients can log into their own portal and view real time information.</p>
    </div>
    <div class="abs col3" style="left:30px;top:518px;width:130px"><h5>Maintenance</h5><p class="body" style="font-size:7.8px;line-height:11.5px">A summary of completed and outstanding jobs can be seen from the Owner Access homepage. You can click through to see when a job was reported, who the assigned supplier is and view any attached images and bills.</p></div>
    <div class="abs col3" style="left:172px;top:518px;width:130px"><h5>Inspections</h5><p class="body" style="font-size:7.8px;line-height:11.5px">Our clients can view inspection reports to see details such as inspection date, images, comments and any suggested follow-up actions.</p></div>
    <div class="abs col3" style="left:314px;top:518px;width:130px"><h5>Inspections</h5><p class="body" style="font-size:7.8px;line-height:11.5px">Our clients can view, download or print current and historical statements, attached bills and general tenancy documents.</p></div>
  </div>
</section>

<!-- Spread 4 -->
<section class="spread" style="top:2450px;background:#f1f1f1">
  <div class="abs" style="left:28px;top:82px"><h2 class="section">Our Services</h2></div>
  <p class="abs" style="left:28px;top:128px;width:410px;font-size:9.6px;line-height:16px;font-weight:600;font-style:italic;color:var(--green)">Lorem Ipsum is simply dummy text of the printing and typesetting industry. Lorem Ipsum has been the industry's standard dummy text ever since the 1500s, when an unknown printer took a galley of type and scrambled it to make a type specimen book.</p>
  <p class="abs body" style="left:497px;top:96px;width:196px">Lorem ipsum dolor sit amet, consectetur adipiscing elit, sed do eiusmod tempor incididunt ut labore et dolore magna aliqua. Ut enim ad minim veniam, quis nostrud exercitation ullamco laboris nisi ut aliquip ex ea commodo consequat. Duis aute irure dolor in reprehenderit in voluptate velit esse cillum dolore eu fugiat nulla pariatur.</p>
  <p class="abs body" style="left:711px;top:96px;width:196px">Lorem ipsum dolor sit amet, consectetur adipiscing elit, sed do eiusmod tempor incididunt ut labore et dolore magna aliqua. Ut enim ad minim veniam, quis nostrud exercitation ullamco laboris nisi ut aliquip ex ea commodo consequat. Duis aute irure dolor in reprehenderit in voluptate velit esse cillum dolore eu fugiat nulla pariatur.</p>
  <div class="services-band">
    <div class="svc" style="left:31px"><div class="hex"><svg viewBox="0 0 32 32"><rect x="5" y="6" width="22" height="15"/><polyline points="8,17 13,12 17,15 23,9"/><line x1="16" y1="21" x2="16" y2="25"/><line x1="11" y1="26" x2="21" y2="26"/></svg></div><h4>Management Fee</h4><p>Lorem ipsum dolor sit amet, consectetur adipiscing elit, sed do eiusmod tempor incididunt ut labore et dolore magna aliqua.</p></div>
    <div class="svc" style="left:168px"><div class="hex"><svg viewBox="0 0 32 32"><rect x="5" y="6" width="22" height="15"/><polyline points="8,17 13,12 17,15 23,9"/><line x1="16" y1="21" x2="16" y2="25"/><line x1="11" y1="26" x2="21" y2="26"/></svg></div><h4>Let Fee</h4><p>Lorem ipsum dolor sit amet, consectetur adipiscing elit, sed do eiusmod tempor incididunt ut labore et dolore magna aliqua.</p></div>
    <div class="svc" style="left:306px"><div class="hex"><svg viewBox="0 0 32 32"><rect x="5" y="6" width="22" height="15"/><polyline points="8,17 13,12 17,15 23,9"/><line x1="16" y1="21" x2="16" y2="25"/><line x1="11" y1="26" x2="21" y2="26"/></svg></div><h4>Marketing Package</h4><p>Lorem ipsum dolor sit amet, consectetur adipiscing elit, sed do eiusmod tempor incididunt ut labore et dolore magna aliqua.</p></div>
    <div class="svc" style="left:495px"><div class="hex"><svg viewBox="0 0 32 32"><rect x="5" y="6" width="22" height="15"/><polyline points="8,17 13,12 17,15 23,9"/><line x1="16" y1="21" x2="16" y2="25"/><line x1="11" y1="26" x2="21" y2="26"/></svg></div><h4>EOFY Fee</h4><p>Lorem ipsum dolor sit amet, consectetur adipiscing elit, sed do eiusmod tempor incididunt ut labore et dolore magna aliqua.</p></div>
    <div class="svc" style="left:633px"><div class="hex"><svg viewBox="0 0 32 32"><rect x="5" y="6" width="22" height="15"/><polyline points="8,17 13,12 17,15 23,9"/><line x1="16" y1="21" x2="16" y2="25"/><line x1="11" y1="26" x2="21" y2="26"/></svg></div><h4>Admin Fee</h4><p>Lorem ipsum dolor sit amet, consectetur adipiscing elit, sed do eiusmod tempor incididunt ut labore et dolore magna aliqua.</p></div>
    <div class="svc" style="left:771px"><div class="hex"><svg viewBox="0 0 32 32"><rect x="5" y="6" width="22" height="15"/><polyline points="8,17 13,12 17,15 23,9"/><line x1="16" y1="21" x2="16" y2="25"/><line x1="11" y1="26" x2="21" y2="26"/></svg></div><h4>Lease Renewal</h4><p>Lorem ipsum dolor sit amet, consectetur adipiscing elit, sed do eiusmod tempor incididunt ut labore et dolore magna aliqua.</p></div>
  </div>
  <div class="photo ph-city" role="img" aria-label="Panoramic city skyline reflected on water" style="left:0;top:453px;width:934px;height:207px"></div>
  <div class="abs" style="left:466px;top:0;width:1px;height:220px;background:#ddd"></div>
</section>

<!-- Spread 5 -->
<section class="spread" style="top:3227px">
  <div class="page left">
    <div class="tab" style="left:0;top:44px;width:185px">House &amp; Land</div>
    <div class="tab-stripe" style="left:195px;top:44px"></div>
    <div class="list-head" style="top:96px">Default of Rent as a result of your tenant:</div>
    <ul class="list" style="top:118px">
      <li>Hardship<span>Up to 18 weeks</span></li>
      <li>Absconding<span>Up to 18 weeks</span></li>
      <li>Failing to give vacant possession defaulting on rent<span>Up to 18 weeks</span></li>
    </ul>
    <div class="list-head" style="top:199px">Loss of Rent following:</div>
    <ul class="list" style="top:220px">
      <li>A defined event<span>Up to 52 weeks</span></li>
      <li>Death of sole tenant (Any location)<span>Up to 52 weeks</span></li>
      <li>Prevention of access following defined peril loss<span>Up to 52 weeks</span></li>
    </ul>
    <div class="list-head" style="top:302px">Damage as a result of:</div>
    <ul class="list" style="top:322px">
      <li>Deliberate &amp; Malicious Damage<span>Up to $60,000</span></li>
      <li>Theft by tenants<span>Up to $60,000</span></li>
      <li>Defined perils including flood<span>Up to $60,000</span></li>
      <li>Accidental Damage including Pet damage*<span>Up to $60,000</span></li>
    </ul>
    <div class="tab" style="left:0;top:435px;width:215px">Rental Guarantee</div>
    <div class="tab-stripe" style="left:225px;top:435px"></div>
    <div class="opt" style="left:36px"><h5>Option 1:</h5><ul><li>1 years</li><li>5%</li><li>Professional Photos</li><li>Landlord Insurance</li></ul></div>
    <div class="opt" style="left:176px"><h5>Option 2:</h5><ul><li>2 years</li><li>4.5%</li><li>Professional Photos</li><li>Landlord Insurance</li></ul></div>
    <div class="opt" style="left:317px"><h5>Option 3:</h5><ul><li>3 years</li><li>4%</li><li>Professional Photos</li><li>Landlord Insurance</li></ul></div>
  </div>
  <div class="page right">
    <div class="photo ph-house" role="img" aria-label="Two-storey suburban house" style="left:0;top:0;width:231px;height:147px"></div>
    <div class="photo ph-house b" role="img" aria-label="House with lit windows at dusk" style="left:236px;top:0;width:231px;height:147px"></div>
    <div class="photo ph-house c" role="img" aria-label="White weatherboard house with lawn" style="left:0;top:151px;width:231px;height:147px"></div>
    <div class="photo ph-house d" role="img" aria-label="Modern family home at twilight" style="left:236px;top:151px;width:231px;height:147px"></div>
    <div class="tab" style="left:0;top:306px;width:410px">Gladstone's Fastest Growing Property Group</div>
    <div class="tab-stripe" style="left:420px;top:306px"></div>
    <div class="service" style="left:34px;top:351px;width:186px">
      <div class="hex"><svg viewBox="0 0 32 32"><path d="M6 8h20v4a4 4 0 0 1-4 4H10a4 4 0 0 1-4-4z"/><line x1="11" y1="19" x2="11" y2="25"/><line x1="16" y1="19" x2="16" y2="26"/><line x1="21" y1="19" x2="21" y2="25"/></svg></div>
      <h4 style="font-weight:400">Smoke Alarm</h4>
      <p>Lorem ipsum dolor sit amet, consectetur adipiscing elit, sed do eiusmod tempor incididunt ut labore et dolore magna aliqua. Ut enim ad minim veniam, quis nostrud exercitation ullamco laboris nisi ut aliquip ex ea commodo consequat. Duis aute irure dolor in reprehenderit in voluptate velit esse cillum dolore eu fugiat nulla pariatur.</p>
    </div>
    <div class="service" style="left:250px;top:351px;width:186px">
      <div class="hex"><svg viewBox="0 0 32 32"><path d="M8 14 16 8l8 6"/><rect x="11" y="13" width="10" height="6"/><path d="M4 22c4 0 6-2 10-2h6c2 0 2 3 0 3h-5"/><path d="M4 26h14l9-6"/></svg></div>
      <h4 style="font-weight:400">Insurance</h4>
      <p>Lorem ipsum dolor sit amet, consectetur adipiscing elit, sed do eiusmod tempor incididunt ut labore et dolore magna aliqua. Ut enim ad minim veniam, quis nostrud exercitation ullamco laboris nisi ut aliquip ex ea commodo consequat. Duis aute irure dolor in reprehenderit in voluptate velit esse cillum dolore eu fugiat nulla pariatur.</p>
    </div>
  </div>
</section>

</body>
</html>
```